business card for a massage therapy practice named 'Meadow and Willow Massage Studio'

I really need a trendy, yet easy on the eyes business card to complement my logo. Ideally with some gold or rose gold foil work.

My uploaded file of the logo I have in horizontal but I have a vertical version as well. Another color that is used in the website is a blush pink here and there. I'd like to see some trendy tropical leaves in the design.

```html
<!DOCTYPE html>
<html lang="en">
<head>
<meta charset="utf-8">
<title>Meadow and Willow Massage Studio – Business Card</title>
<link href="https://fonts.googleapis.com/css2?family=Montserrat:wght@400;500&family=Barlow:wght@300;400;600&display=swap" rel="stylesheet">
<style>
  :root {
    --page: #e8e8e6;
    --forest-deep: #163a3d;
    --forest-mid: #2b4b43;
    --forest-olive: #4e6446;
    --panel: rgba(236, 241, 241, 0.94);
    --ink: #1d3f44;
    --ink-soft: #34565b;
    --gold: #a88f55;
    --white: #ffffff;
  }
  * { margin: 0; padding: 0; box-sizing: border-box; }
  html, body {
    width: 1200px; height: 1200px; overflow: hidden;
    background: var(--page);
  }
  .canvas { position: relative; width: 1200px; height: 1200px; }
  .card {
    position: absolute; left: 178px; width: 844px; height: 506px;
    overflow: hidden;
  }
  .card--front { top: 44px; }
  .card--back { top: 620px; }
  .foliage {
    position: absolute; inset: 0;
    background:
      radial-gradient(ellipse at 70% 40%, rgba(110,125,80,0.45), transparent 60%),
      radial-gradient(ellipse at 20% 80%, rgba(90,110,70,0.35), transparent 55%),
      linear-gradient(135deg, var(--forest-deep) 0%, var(--forest-mid) 55%, var(--forest-olive) 100%);
  }
  .front-panel {
    position: absolute; left: 49px; top: 49px; right: 49px; bottom: 49px;
    background: var(--panel);
  }
  .divider {
    position: absolute; left: 374px; top: 41px; width: 3px; height: 326px;
    background: var(--ink);
  }
  .identity {
    position: absolute; left: 0; top: 0; width: 374px; height: 100%;
    text-align: center; font-family: "Montserrat", sans-serif; color: var(--ink);
  }
  .brand-name {
    position: absolute; left: 0; right: 0; top: 128px;
    font-family: "Montserrat", sans-serif; font-weight: 500;
    font-size: 19px; line-height: 1.3; color: var(--gold); letter-spacing: 0.02em;
  }
  .brand-name::before {
    content: ""; display: inline-block; width: 10px; height: 10px;
    border-radius: 50%; background: var(--gold); margin-right: 8px; vertical-align: middle;
  }
  .person-name {
    position: absolute; left: 0; right: 0; top: 228px;
    font-weight: 500; font-size: 42px; line-height: 1;
  }
  .person-title {
    position: absolute; left: 0; right: 0; top: 284px;
    font-family: "Barlow", sans-serif; font-weight: 400;
    font-size: 16px; letter-spacing: 0.28em;
  }
  .contact {
    position: absolute; left: 420px; top: 150px;
    font-family: "Barlow", sans-serif; font-weight: 300;
    font-size: 18px; color: var(--ink-soft); list-style: none;
  }
  .contact li { height: 36px; line-height: 36px; }
  .frames { position: absolute; inset: 0; }
  .back-brand {
    position: absolute; left: 0; width: 844px; top: 226px; text-align: center;
    font-family: "Montserrat", sans-serif; font-weight: 500;
    font-size: 30px; color: var(--white); letter-spacing: 0.02em;
  }
  .back-brand::before {
    content: ""; display: inline-block; width: 14px; height: 14px;
    border-radius: 50%; background: var(--white); margin-right: 12px; vertical-align: middle;
  }
  .back-web {
    position: absolute; left: 0; width: 844px; top: 390px; text-align: center;
    font-family: "Barlow", sans-serif; font-weight: 600;
    font-size: 14px; color: var(--white); letter-spacing: 0.04em;
  }
</style>
</head>
<body>
<main class="canvas">
  <section class="card card--front">
    <div class="foliage" role="img" aria-label="Dark green tropical leaves with water droplets"></div>
    <div class="front-panel">
      <div class="identity">
        <p class="brand-name">Meadow and Willow<br>Massage Studio</p>
        <h1 class="person-name">Deniz Aral</h1>
        <p class="person-title">GENERAL MANAGER</p>
      </div>
      <div class="divider"></div>
      <ul class="contact">
        <li>Email: hello@meadowwillow.com</li>
        <li>Address: 2715 Izmir / Turkey</li>
        <li>Phone: +90 512 608 27 19</li>
        <li>Website: www.meadowwillow.com</li>
      </ul>
    </div>
  </section>

  <section class="card card--back">
    <div class="foliage" role="img" aria-label="Dark green tropical leaves with water droplets"></div>
    <svg class="frames" width="844" height="506" viewBox="0 0 844 506">
      <rect x="82" y="50" width="712" height="372" fill="none" stroke="#ffffff" stroke-width="4"/>
      <rect x="51" y="85" width="712" height="370" fill="none" stroke="#ffffff" stroke-width="4"/>
    </svg>
    <p class="back-brand">Meadow and Willow Massage Studio</p>
    <p class="back-web">WWW.MEADOWWILLOW.COM</p>
  </section>
</main>
</body>
</html>
```